Design a Banner for international cricket website

Design a beautiful banner related to international cricket with High Definition color. It should have 5 rotating different images. Logo should be on the left as you can see in the image attached.

```html
<!DOCTYPE html>
<html lang="en">
<head>
<meta charset="UTF-8">
<title>PitchPoint – International Cricket</title>
<link rel="stylesheet" href="https://fonts.googleapis.com/css2?family=Exo+2:wght@700;800&display=swap">
<style>
  :root {
    --ink: #000000;
    --night-blue: #04102a;
    --deep-blue: #0a2a70;
    --kit-blue: #2f74d6;
    --cap-blue: #4f95ec;
    --glow-blue: #7fc0ff;
    --skin-warm: #6b4632;
    --band-magenta: #b41fc6;
    --band-dark: #5e0878;
    --band-light: #f4c2ff;
    --brand-orange: #f28a1c;
    --text-light: #ffffff;
  }
  * { margin: 0; padding: 0; box-sizing: border-box; }
  html, body {
    width: 1200px;
    height: 264px;
    overflow: hidden;
    background: var(--ink);
  }
  .banner {
    position: relative;
    width: 1200px;
    height: 264px;
    overflow: hidden;
    background: var(--ink);
    font-family: "Exo 2", sans-serif;
  }
  .team-photo {
    position: absolute;
    left: 290px;
    top: 0;
    width: 910px;
    height: 264px;
    background:
      radial-gradient(ellipse 90px 60px at 265px 40px, rgba(127,192,255,0.85), transparent 75%),
      radial-gradient(ellipse 80px 55px at 720px 60px, rgba(127,192,255,0.8), transparent 75%),
      radial-gradient(ellipse 85px 55px at 840px 80px, rgba(127,192,255,0.75), transparent 75%),
      radial-gradient(ellipse 70px 50px at 440px 110px, rgba(79,149,236,0.85), transparent 75%),
      radial-gradient(ellipse 70px 50px at 610px 100px, rgba(79,149,236,0.85), transparent 75%),
      radial-gradient(ellipse 60px 45px at 540px 150px, rgba(107,70,50,0.7), transparent 75%),
      radial-gradient(ellipse 55px 45px at 300px 110px, rgba(107,70,50,0.6), transparent 75%),
      radial-gradient(ellipse 55px 45px at 800px 150px, rgba(107,70,50,0.6), transparent 75%),
      radial-gradient(ellipse 420px 130px at 540px 220px, rgba(47,116,214,0.9), transparent 75%),
      radial-gradient(ellipse 200px 120px at 130px 60px, rgba(47,116,214,0.5), transparent 75%),
      linear-gradient(180deg, var(--deep-blue) 0%, var(--night-blue) 100%);
  }
  .team-photo::before {
    content: "";
    position: absolute;
    inset: 0;
    background: linear-gradient(90deg, var(--ink) 0%, rgba(0,0,0,0.55) 10%, transparent 24%);
  }
  .brand {
    position: absolute;
    left: 22px;
    top: 98px;
    display: flex;
    align-items: center;
    gap: 12px;
  }
  .brand-dot {
    width: 34px;
    height: 34px;
    border-radius: 50%;
    background: var(--brand-orange);
  }
  .brand-name {
    color: var(--brand-orange);
    font-size: 46px;
    font-weight: 800;
    line-height: 1;
  }
  .title-band {
    position: absolute;
    left: 360px;
    top: 194px;
    width: 840px;
    height: 54px;
    background:
      linear-gradient(180deg, rgba(255,255,255,0.3) 0%, transparent 45%, rgba(0,0,0,0.2) 100%),
      linear-gradient(90deg, var(--band-light) 0%, var(--band-magenta) 15%, var(--band-magenta) 62%, var(--band-dark) 100%);
  }
  .title-text {
    position: absolute;
    left: 170px;
    right: 110px;
    top: 0;
    height: 54px;
    display: flex;
    align-items: center;
    justify-content: center;
    color: var(--text-light);
    font-size: 38px;
    font-weight: 700;
    letter-spacing: 5px;
    text-shadow: 0 2px 3px rgba(60,0,80,0.7);
    white-space: nowrap;
  }
</style>
</head>
<body>
  <header class="banner">
    <div class="team-photo" role="img" aria-label="Cricket team in blue kits and caps huddling together to celebrate a wicket, against a blue stadium screen"></div>
    <div class="brand">
      <span class="brand-dot"></span>
      <span class="brand-name">PitchPoint</span>
    </div>
    <div class="title-band">
      <h1 class="title-text">International Cricket</h1>
    </div>
  </header>
</body>
</html>
```